Redesign Of Current Landing Page

I need to redesign this landing page https://www.brightoakpromos.biz/?page=landing&landing=23 (Please do not opt in because when you do it will show you the home page. Please clear your cookies before going to this url above to view the 1 page landing page.)

Please use my updated website as a reference for colors and logo.
http://layoutcraftzone.com/dh/bopg/index.html

I would like the call to action to be a button that opens into a lead form...

Button would be "Download Samples"

small business owners

Marketing

1 page

Designer to choose colors to be used in the design.

• must be full responsive on all devices
• must have a legitimate professional apeal to it
• open

```html
<!DOCTYPE html>
<html lang="en">
<head>
<meta charset="utf-8">
<title>Bright Oak Promos – Landing</title>
<link href="https://fonts.googleapis.com/css2?family=Poppins:wght@300;400;500;600;700&display=swap" rel="stylesheet">
<style>
:root{
  --blue:#1a6fbf;
  --blue-dark:#0f5aa0;
  --ink:#1d1d1f;
  --text:#555b63;
  --muted:#8a9097;
  --light:#f1f2f4;
  --line:#e1e3e6;
  --white:#ffffff;
  --dark:#3a3a3c;
}
*{box-sizing:border-box;margin:0;padding:0}
html,body{width:1200px;height:3956px;overflow:hidden}
body{font-family:'Poppins',sans-serif;color:var(--text);background:var(--white);position:relative}
.wrap{width:830px;margin:0 auto;position:relative}

/* header */
.site-header{height:118px;background:var(--white);border-bottom:1px solid var(--line)}
.header-top{display:flex;justify-content:space-between;align-items:center;height:62px}
.brand{display:flex;align-items:center;gap:8px}
.brand-dot{width:22px;height:22px;border-radius:50%;background:var(--blue)}
.brand-name{font-weight:700;font-size:26px;color:var(--ink);letter-spacing:1px}
.contact-bar{display:flex;align-items:center;gap:10px;font-size:10px;color:var(--text)}
.contact-bar b{font-weight:600;color:var(--ink)}
.pill{display:inline-block;padding:5px 16px;border-radius:14px;font-size:10px;color:var(--white);font-weight:500}
.pill.login{background:var(--blue)}
.pill.signup{background:#8a8d91}
.main-nav{display:flex;justify-content:space-between;align-items:center;height:40px}
.main-nav a{font-size:13px;font-weight:600;color:var(--ink);text-decoration:none;padding:4px 20px}
.main-nav a.active{background:var(--blue);color:var(--white);border-radius:14px}

/* hero */
.hero{height:523px;position:relative;background:linear-gradient(90deg,#f7f7f8 0%,#eef0f2 45%,#c8ccd2 70%,#5b6470 100%)}
.hero-photo{position:absolute;right:0;top:0;width:560px;height:100%;background:linear-gradient(100deg,rgba(240,241,243,0) 0%,#b9bec6 35%,#4d5663 75%,#2f3742 100%)}
.hero-copy{position:absolute;left:198px;top:150px;width:420px}
.hero-copy h1{font-size:22px;font-weight:400;line-height:34px;color:var(--ink)}
.btn{display:inline-block;background:var(--blue);color:var(--white);font-weight:600;font-size:16px;border-radius:24px;text-align:center;text-decoration:none}
.hero .btn{margin-top:22px;width:230px;height:48px;line-height:48px}
.slider-dots{position:absolute;left:32px;top:328px;display:flex;flex-direction:column;gap:18px}
.slider-dots span{width:11px;height:11px;border-radius:50%;background:#b7bcc2}
.slider-dots span.on{background:var(--blue)}

/* stats */
.stats{height:264px;background:var(--light);padding-top:56px}
.stats-list{display:flex;justify-content:space-between;width:830px;margin:0 auto}
.stat{width:115px;text-align:center}
.stat-icon{width:112px;height:112px;border-radius:50%;background:var(--blue);border:4px solid #d6e4f3;display:flex;align-items:center;justify-content:center;margin:0 auto}
.stat p{font-size:9px;line-height:13px;color:var(--ink);margin-top:16px}

/* process */
.process{height:664px;padding-top:78px}
.section-title{text-align:center;font-size:20px;font-weight:600;color:var(--ink)}
.process-cards{display:flex;justify-content:space-between;width:830px;margin:58px auto 0}
.process-card{width:190px;height:340px;background:var(--light);border:1px solid var(--line);border-radius:6px;position:relative;text-align:center;padding:108px 20px 0}
.process-card.featured{background:var(--blue);border-color:var(--blue)}
.process-icon{position:absolute;left:50%;top:-54px;transform:translateX(-50%);width:104px;height:104px;border-radius:50%;background:var(--blue);border:6px solid var(--white);display:flex;align-items:center;justify-content:center}
.process-card.featured .process-icon{box-shadow:0 0 0 2px var(--blue)}
.process-card h3{font-size:16px;font-weight:600;color:var(--blue);line-height:22px}
.process-card.featured h3,.process-card.featured p{color:var(--white)}
.process-card p{font-size:10px;line-height:16px;color:var(--text);margin-top:28px}

/* what we do */
.services{height:575px;position:relative;background:linear-gradient(160deg,#56565a 0%,#3b3b3e 50%,#2b2b2d 100%);padding-top:96px}
.services .section-title{color:var(--white)}
.service-list{display:flex;justify-content:space-between;width:830px;margin:44px auto 0}
.service{width:190px;text-align:center}
.service-icon{width:88px;height:88px;border-radius:50%;background:var(--blue);margin:0 auto;display:flex;align-items:center;justify-content:center}
.service h4{color:var(--white);font-size:14px;font-weight:500;margin-top:18px}
.service p{color:#d9d9db;font-size:9px;line-height:14px;margin-top:10px}
.services .btn{display:block;width:230px;height:46px;line-height:46px;margin:66px auto 0;font-size:16px}

/* video */
.video{height:704px;padding-top:50px}
.video-frame{width:794px;height:422px;margin:30px auto 0;border:8px solid #d3d5d8;position:relative;background:linear-gradient(120deg,#2a3a52 0%,#4f79a6 40%,#8fb7d4 70%,#c79b7c 100%)}
.play{position:absolute;left:50%;top:50%;width:84px;height:84px;margin:-42px 0 0 -42px;border-radius:50%;background:rgba(255,255,255,.55);display:flex;align-items:center;justify-content:center}
.video .btn{display:block;width:230px;height:46px;line-height:46px;margin:54px auto 0}

/* testimonials */
.testimonials{height:464px;background:linear-gradient(180deg,#2573bd,#1a65ae);position:relative;padding-top:84px}
.testimonials .section-title{color:var(--white)}
.testimonial{position:absolute;left:264px;top:170px;display:flex;gap:34px;width:690px}
.avatar{width:164px;height:164px;border-radius:50%;border:6px solid var(--white);background:linear-gradient(160deg,#8d6c58,#c9a48a);flex:none}
.quote h5{color:var(--white);font-size:18px;font-weight:600;margin-top:10px}
.quote p{color:#e4eefa;font-size:13px;line-height:22px;margin-top:8px}
.arrow{position:absolute;top:248px;color:var(--white)}
.arrow.prev{left:112px}.arrow.next{left:1068px}
.btn-outline{position:absolute;left:448px;top:375px;width:304px;height:46px;line-height:42px;border:2px solid var(--white);border-radius:24px;color:var(--white);font-size:14px;font-weight:500;text-align:center}

/* partners */
.partners{height:143px;display:flex;align-items:center;justify-content:space-between;padding:0 70px}
.partner{font-size:24px;font-weight:600;color:#555b63}

/* footer */
.site-footer{height:448px;background:var(--light);border-top:1px solid var(--line);position:relative}
.footer-brand{display:flex;justify-content:center;align-items:center;gap:8px;margin-top:44px}
.footer-cols{position:absolute;top:146px;left:185px;width:830px}
.footer-col{position:absolute;top:0}
.footer-col h6{font-size:11px;font-weight:600;color:var(--blue)}
.quick-links{left:0}
.quick-links li{list-style:none;font-size:10px;line-height:20px;color:var(--ink)}
.quick-links ul{margin-top:16px}
.address{left:166px;width:240px}
.address .row{display:flex;gap:14px;font-size:10px;line-height:17px;color:var(--ink);margin-top:16px}
.address svg{flex:none;margin-top:2px}
.contact-form{left:424px;width:410px}
.field{display:block;width:186px;height:32px;border:1px solid #b9bcc0;background:var(--white);font-size:9px;color:var(--muted);padding:9px 8px;margin-top:10px}
.field:first-of-type{margin-top:16px}
.message{position:absolute;left:200px;top:31px;width:190px;height:116px;border:1px solid #b9bcc0;background:var(--white);font-size:9px;color:var(--muted);padding:9px 8px}
.submit{display:inline-block;margin-top:14px;background:var(--blue);color:var(--white);font-size:10px;font-weight:600;padding:8px 18px}
.bottom-bar{position:absolute;left:0;bottom:0;width:1200px;height:53px;text-align:center;line-height:53px;font-size:10px;color:var(--ink);background:var(--white)}
</style>
</head>
<body>

<header class="site-header">
  <div class="wrap header-top">
    <div class="brand"><span class="brand-dot"></span><span class="brand-name">BOPG</span></div>
    <div class="contact-bar">
      <svg width="12" height="12" viewBox="0 0 24 24"><circle cx="12" cy="12" r="12" fill="#1a6fbf"/><path d="M8 6l2 3-1.5 1.5a8 8 0 004 4L14 13l3 2-1 2.5C10 17 7 14 6.5 8z" fill="#fff"/></svg>
      <span><b>USA Office :</b> 800-555-0142</span><span>|</span><span><b>International :</b> 1-800-555-0199</span>
      <span class="pill login">LOGIN</span><span class="pill signup">SIGN UP</span>
    </div>
  </div>
  <nav class="wrap main-nav">
    <a class="active">HOME</a><a>OUR INCENTIVES</a><a>SAMPLES</a><a>AFFILIATES</a><a>TESTIMONIALS</a><a>FAQ</a><a>CONTACT</a>
  </nav>
</header>

<section class="hero">
  <div class="hero-photo" role="img" aria-label="Photo of a customer service agent with a headset in a bright office"></div>
  <div class="slider-dots"><span class="on"></span><span></span><span></span><span></span></div>
  <div class="hero-copy">
    <h1>Increase Leads &amp; Sales From Your Existing Marketing Efforts By Offering High Perceived Value Incentives To Your Customers!</h1>
    <a class="btn">Download Samples</a>
  </div>
</section>

<section class="stats">
  <div class="stats-list">
    <div class="stat"><div class="stat-icon"><svg width="52" height="52" viewBox="0 0 52 52" fill="none" stroke="#fff" stroke-width="2"><path d="M6 46h40M6 46V6"/><path d="M10 38l10-12 8 6 14-18"/><path d="M36 14h6v6"/></svg></div><p>12 Years In Business</p></div>
    <div class="stat"><div class="stat-icon"><svg width="52" height="52" viewBox="0 0 52 52" fill="none" stroke="#fff" stroke-width="2"><circle cx="26" cy="18" r="8"/><path d="M12 44c0-9 6-14 14-14s14 5 14 14"/><circle cx="10" cy="22" r="5"/><circle cx="42" cy="22" r="5"/></svg></div><p>13,000+ Clients Enrolled</p></div>
    <div class="stat"><div class="stat-icon"><svg width="52" height="52" viewBox="0 0 52 52" fill="none" stroke="#fff" stroke-width="2"><circle cx="26" cy="22" r="13"/><circle cx="26" cy="22" r="7"/><path d="M18 33l-4 13 6-3 4 5 2-10M34 33l4 13-6-3-4 5"/></svg></div><p>3+ Million Certificates Distributed</p></div>
    <div class="stat"><div class="stat-icon"><svg width="52" height="52" viewBox="0 0 52 52" fill="none" stroke="#fff" stroke-width="2"><path d="M16 8h20v12a10 10 0 01-20 0z"/><path d="M16 12H8c0 8 4 11 9 11M36 12h8c0 8-4 11-9 11"/><path d="M26 30v8M18 44h16v-6H18z"/></svg></div><p>100's Of Thousands Of Redemptions</p></div>
    <div class="stat"><div class="stat-icon"><svg width="44" height="52" viewBox="0 0 44 52"><rect x="4" y="4" width="36" height="44" rx="4" fill="#fff"/></svg></div><p>A+ Business Rating</p></div>
    <div class="stat"><div class="stat-icon"><svg width="52" height="52" viewBox="0 0 52 52" fill="none" stroke="#fff" stroke-width="2"><path d="M12 46V6"/><path d="M12 8h28l-6 9 6 9H12"/></svg></div><p>Licensed Seller Of Travel CST #2048315</p></div>
  </div>
</section>

<section class="process">
  <h2 class="section-title">Our Process</h2>
  <div class="process-cards">
    <div class="process-card featured">
      <div class="process-icon"><svg width="46" height="46" viewBox="0 0 46 46" fill="none" stroke="#fff" stroke-width="2"><path d="M6 32a17 17 0 1134 0"/><path d="M23 32l9-12"/><circle cx="23" cy="32" r="3"/></svg></div>
      <h3>Boost Response Rates To Your Existing Ads</h3>
      <p>By adding a simple tagline "Contact us today and receive Two Nights in Las Vegas, No Purchase Necessary!</p>
    </div>
    <div class="process-card">
      <div class="process-icon"><svg width="46" height="46" viewBox="0 0 46 46" fill="none" stroke="#fff" stroke-width="2"><rect x="6" y="8" width="34" height="24"/><path d="M11 26l8-8 6 5 9-10M16 32l-4 9M30 32l4 9"/></svg></div>
      <h3>Increase Repeat &amp; Referral Business</h3>
      <p>By adding a simple tagline "Contact us today and receive Two Nights in Las Vegas, No Purchase Necessary!</p>
    </div>
    <div class="process-card">
      <div class="process-icon"><svg width="46" height="46" viewBox="0 0 46 46" fill="none" stroke="#fff" stroke-width="2"><circle cx="23" cy="10" r="5"/><path d="M14 24c0-5 4-8 9-8s9 3 9 8"/><circle cx="9" cy="32" r="4"/><circle cx="37" cy="32" r="4"/><path d="M23 24v6M9 28l14-4 14 4"/></svg></div>
      <h3>Get More New Customers</h3>
      <p>By adding a simple tagline "Contact us today and receive Two Nights in Las Vegas, No Purchase Necessary!</p>
    </div>
    <div class="process-card">
      <div class="process-icon"><svg width="46" height="46" viewBox="0 0 46 46" fill="none" stroke="#fff" stroke-width="2"><circle cx="23" cy="13" r="7"/><path d="M10 40c0-9 6-14 13-14s13 5 13 14z"/><rect x="18" y="30" width="10" height="6"/></svg></div>
      <h3>Boost Your Referral Business</h3>
      <p>By adding a simple tagline "Contact us today and receive Two Nights in Las Vegas, No Purchase Necessary!</p>
    </div>
  </div>
</section>

<section class="services" role="img" aria-label="Dimmed photo of business people working at laptops">
  <h2 class="section-title">What We Do ?</h2>
  <div class="service-list">
    <div class="service"><div class="service-icon"><svg width="38" height="38" viewBox="0 0 38 38" fill="#fff"><rect x="10" y="4" width="18" height="9"/><rect x="4" y="14" width="30" height="13" rx="2"/><rect x="10" y="23" width="18" height="11" stroke="#1a6fbf" stroke-width="2"/></svg></div><h4>Print</h4><p>Download PDF certificates to print and physically hand them out or mail them to your customers.</p></div>
    <div class="service"><div class="service-icon"><svg width="38" height="38" viewBox="0 0 38 38" fill="none" stroke="#fff" stroke-width="2.5"><rect x="5" y="9" width="28" height="20" rx="2"/><path d="M5 11l14 10 14-10"/></svg></div><h4>E-Mail</h4><p>Download PDF certificates to print and physically hand them out or mail them to your customers.</p></div>
    <div class="service"><div class="service-icon"><svg width="38" height="38" viewBox="0 0 38 38" fill="none" stroke="#fff" stroke-width="2.5"><circle cx="19" cy="19" r="13"/><path d="M6 19h26M19 6c-6 7-6 19 0 26M19 6c6 7 6 19 0 26"/></svg></div><h4>Online Automation</h4><p>Download PDF certificates to print and physically hand them out or mail them to your customers.</p></div>
    <div class="service"><div class="service-icon"><svg width="38" height="38" viewBox="0 0 38 38" fill="none" stroke="#fff" stroke-width="2.5"><rect x="4" y="10" width="30" height="18" rx="2"/><path d="M9 15h2M14 15h2M19 15h2M24 15h2M12 23h14"/></svg></div><h4>Text Messaging</h4><p>Download PDF certificates to print and physically hand them out or mail them to your customers.</p></div>
  </div>
  <a class="btn">Download Samples</a>
</section>

<section class="video">
  <h2 class="section-title">Featured Video</h2>
  <div class="video-frame" role="img" aria-label="Video still of a presenter in a suit in front of a collage of vacation scenes">
    <div class="play"><svg width="34" height="34" viewBox="0 0 34 34"><path d="M10 5l20 12-20 12z" fill="#fff"/></svg></div>
  </div>
  <a class="btn">Watch Video Now</a>
</section>

<section class="testimonials">
  <h2 class="section-title">Client Testimonials</h2>
  <svg class="arrow prev" width="14" height="20" viewBox="0 0 14 20"><path d="M11 2L3 10l8 8" stroke="#fff" stroke-width="3" fill="none"/></svg>
  <div class="testimonial">
    <div class="avatar" role="img" aria-label="Portrait photo of the client"></div>
    <div class="quote">
      <h5>Marla T.</h5>
      <p>Bright Oak Promos has helped my massage business grow exponentially in the last 2 years. It is the easiest and most-affordable way to reward loyal customers, as well as, employees! Thanks BOP!</p>
    </div>
  </div>
  <svg class="arrow next" width="14" height="20" viewBox="0 0 14 20"><path d="M3 2l8 8-8 8" stroke="#fff" stroke-width="3" fill="none"/></svg>
  <div class="btn-outline">Sign Up For 30 Day Risk Free Trail</div>
</section>

<section class="partners">
  <span class="partner">Hearthline</span>
  <span class="partner">Fieldcrest</span>
  <span class="partner">Keystone Realty</span>
  <span class="partner">Velora Motors</span>
  <span class="partner">Parcelon</span>
  <span class="partner">Granitewell</span>
</section>

<footer class="site-footer">
  <div class="footer-brand"><span class="brand-dot"></span><span class="brand-name">BOPG</span></div>
  <div class="footer-cols">
    <div class="footer-col quick-links">
      <h6>Quick Links</h6>
      <ul><li>Home</li><li>Our Incentives</li><li>Samples</li><li>Affiliate</li><li>Testimonials</li><li>Faq</li><li>Contact Us</li><li>Terms &amp; Conditions</li><li>Privacy Policy</li></ul>
    </div>
    <div class="footer-col address">
      <h6>Address</h6>
      <div class="row"><svg width="10" height="13" viewBox="0 0 10 13"><path d="M5 0a5 5 0 015 5c0 4-5 8-5 8S0 9 0 5a5 5 0 015-5z" fill="#1a6fbf"/><circle cx="5" cy="5" r="2" fill="#fff"/></svg><span>Bright Oak Promo Group, Inc.<br>418 Harbor Lane<br>Suncrest CA 90210</span></div>
      <div class="row"><svg width="12" height="12" viewBox="0 0 24 24"><path d="M5 2l5 5-3 3a13 13 0 007 7l3-3 5 5-3 3C10 22 2 14 2 5z" fill="#1a6fbf"/></svg><span>800-555-0142<br>1-800-555-0199</span></div>
      <div class="row"><svg width="12" height="12" viewBox="0 0 24 24"><circle cx="12" cy="12" r="11" fill="#1a6fbf"/><path d="M12 6v6l4 3" stroke="#fff" stroke-width="2" fill="none"/></svg><span>Hours: Mon-Fri 7am - 4pm PST<br>Sat-Sun CLOSED</span></div>
    </div>
    <div class="footer-col contact-form">
      <h6>Contact Us</h6>
      <span class="field">Name</span>
      <span class="field">E-mail</span>
      <span class="field">Phone</span>
      <span class="message">Message</span>
      <span class="submit">SUBMIT</span>
    </div>
  </div>
  <div class="bottom-bar">© 2017 Company Name &nbsp;|&nbsp; All Rights Reserved</div>
</footer>

</body>
</html>
```